Business card design needed for a security services business.

We provide a wide range of security services from guard personnel to electronic systems.

Industry/Entity Type

Security Industry

Contact Information for Business Card

Brent Holloway, Owner Office: 780.555.0148; Cell: 780.555.0193 Email: brent@korvanshieldgroup.example; Address 20417 163 St Edmonton, AB T5X 2K8

Colors
0054AA
0677BA
7BADD7
CADEEF
E8F1F8

Requirements
Nice to have
• On the back of the card I would like to possible list the services I provide: Guards Mobiles Live Video Surveillance Access Intrusion

```html
<!DOCTYPE html>
<html lang="en">
<head>
<meta charset="utf-8">
<title>Korvan Shield Group – Business Card</title>
<link href="https://fonts.googleapis.com/css2?family=Poppins:wght@400;600;700&display=swap" rel="stylesheet">
<style>
  :root {
    --bg: #777777;
    --card-light: #ffffff;
    --card-dark: #1e1b1c;
    --brand-blue: #0a6fbf;
    --ink: #111111;
    --muted: #6a6a6a;
    --service-text: #cfcfcf;
    --rule: #6d6d6d;
  }
  html, body {
    margin: 0;
    padding: 0;
    width: 1065px;
    height: 1200px;
    overflow: hidden;
    background: var(--bg);
    font-family: "Poppins", sans-serif;
  }
  .canvas {
    position: relative;
    width: 1065px;
    height: 1200px;
  }
  .card {
    position: absolute;
    width: 583px;
    height: 363px;
    box-shadow: 2px 3px 3px rgba(0,0,0,0.55);
  }
  .card-front {
    left: 292px;
    top: 218px;
    background: var(--card-light);
    border-radius: 0 181.5px 181.5px 0;
  }
  .card-back {
    left: 263px;
    top: 623px;
    background: var(--card-dark);
    border-radius: 181.5px 0 0 181.5px;
  }
  .front-brand {
    position: absolute;
    left: 150px;
    top: 67px;
    height: 242px;
    writing-mode: vertical-rl;
    transform: rotate(180deg);
    font-weight: 600;
    font-size: 22px;
    letter-spacing: 1px;
    color: var(--brand-blue);
    text-align: center;
    white-space: nowrap;
  }
  .front-rule {
    position: absolute;
    left: 195px;
    top: 67px;
    width: 1.5px;
    height: 242px;
    background: var(--rule);
  }
  .holder {
    position: absolute;
    left: 227px;
    top: 82px;
  }
  .holder-name {
    margin: 0;
    font-weight: 700;
    font-size: 25px;
    line-height: 1.1;
    color: var(--brand-blue);
  }
  .holder-role {
    margin: 2px 0 0;
    font-size: 16px;
    color: var(--muted);
  }
  .address {
    position: absolute;
    left: 226px;
    top: 155px;
    font-style: normal;
    font-size: 17px;
    line-height: 21px;
    color: var(--ink);
  }
  .contacts {
    position: absolute;
    left: 225px;
    top: 222px;
    margin: 0;
    padding: 0;
    list-style: none;
    font-size: 17px;
    line-height: 21px;
    color: var(--ink);
  }
  .contacts li {
    display: flex;
    align-items: center;
    gap: 6px;
    white-space: nowrap;
  }
  .contacts .contact-email {
    font-size: 15px;
  }
  .contacts svg {
    width: 16px;
    height: 16px;
    flex: none;
  }
  .back-brand {
    position: absolute;
    left: 0;
    right: 0;
    top: 108px;
    text-align: center;
    font-weight: 600;
    font-size: 30px;
    line-height: 1.15;
    letter-spacing: 1px;
    color: var(--brand-blue);
  }
  .services {
    position: absolute;
    top: 256px;
    margin: 0;
    padding: 0;
    list-style: none;
    font-size: 17px;
    line-height: 21px;
    color: var(--service-text);
    white-space: nowrap;
  }
  .services-left {
    right: calc(583px - 267px);
    text-align: right;
  }
  .services-right {
    left: 306px;
    text-align: left;
  }
  .services-divider {
    position: absolute;
    left: 286px;
    top: 256px;
    width: 1.5px;
    height: 42px;
    background: var(--brand-blue);
  }
</style>
</head>
<body>
<main class="canvas">
  <section class="card card-front" aria-label="Card front">
    <div class="front-brand">KORVAN SHIELD GROUP</div>
    <div class="front-rule"></div>
    <div class="holder">
      <h1 class="holder-name">BRENT HOLLOWAY</h1>
      <p class="holder-role">OWNER</p>
    </div>
    <address class="address">20417 163 St Edmonton<br>AB T5X 2K8</address>
    <ul class="contacts">
      <li>
        <svg viewBox="0 0 16 16" aria-hidden="true"><path d="M3.5 1.5l2.5 3-1.5 1.5c.8 2 2.5 3.7 4.5 4.5L10.5 9l3 2.5-1.5 2.5C7 14 2 9 2 3z" fill="none" stroke="var(--brand-blue)" stroke-width="1.6" stroke-linejoin="round"/></svg>
        780.555.0148
      </li>
      <li>
        <svg viewBox="0 0 16 16" aria-hidden="true"><path d="M3.5 1.5l2.5 3-1.5 1.5c.8 2 2.5 3.7 4.5 4.5L10.5 9l3 2.5-1.5 2.5C7 14 2 9 2 3z" fill="none" stroke="var(--brand-blue)" stroke-width="1.6" stroke-linejoin="round"/></svg>
        780.555.0193
      </li>
      <li class="contact-email">
        <svg viewBox="0 0 16 16" aria-hidden="true"><rect x="0.5" y="3.5" width="15" height="10" fill="var(--brand-blue)"/><path d="M0.5 3.5l7.5 6 7.5-6M0.5 13.5l5.5-5M15.5 13.5l-5.5-5" fill="none" stroke="#fff" stroke-width="1"/></svg>
        brent@korvanshieldgroup.example
      </li>
    </ul>
  </section>

  <section class="card card-back" aria-label="Card back">
    <div class="back-brand">KORVAN SHIELD<br>GROUP</div>
    <ul class="services services-left">
      <li>GUARDS</li>
      <li>MOBILES LIVE</li>
    </ul>
    <div class="services-divider"></div>
    <ul class="services services-right">
      <li>VIDEO SURVEILLANCE</li>
      <li>ACCESS INTRUSION</li>
    </ul>
  </section>
</main>
</body>
</html>
```